Startup internet service provider needs a good facebook ad

Looking for a catchy facebook ad to launch our internet service in Parker, Colorado. Short video or slideshow preferred, still pictures are okay.

https://www.facebook.com/BrimfoxNetworks

www.brimfox-networks.example

Target Market(s)

Parker Colorado

Colors
add136
0255a3

```html
<!DOCTYPE html>
<html lang="en">
<head>
<meta charset="utf-8">
<title>Brimfox Networks – Fast and Reliable Internet</title>
<link rel="stylesheet" href="https://fonts.googleapis.com/css2?family=Montserrat:wght@400;700&display=swap">
<style>
  :root {
    --bg: #161110;
    --lime: #add136;
    --brand-blue: #0255a3;
    --white: #ffffff;
    --fiber-deep: #0a2a5c;
    --fiber-bright: #1f8fe0;
    --fiber-cyan: #39c6e8;
  }
  * { margin: 0; padding: 0; box-sizing: border-box; }
  html, body {
    width: 1200px;
    height: 1200px;
    overflow: hidden;
    background: var(--bg);
  }
  .ad {
    position: relative;
    width: 1200px;
    height: 1200px;
    background: var(--bg);
    font-family: "Montserrat", sans-serif;
    overflow: hidden;
  }
  .brand {
    position: absolute;
    left: 72px;
    top: 68px;
    display: flex;
    align-items: center;
    gap: 16px;
    z-index: 2;
  }
  .brand-dot {
    width: 76px;
    height: 76px;
    border-radius: 50%;
    background: var(--brand-blue);
  }
  .brand-name {
    font-family: "Montserrat", sans-serif;
    font-weight: 400;
    font-size: 36px;
    color: var(--brand-blue);
  }
  .headline {
    position: absolute;
    left: 72px;
    top: 224px;
    width: 1120px;
    font-weight: 700;
    font-size: 69px;
    line-height: 71px;
    color: var(--lime);
    text-transform: uppercase;
    letter-spacing: -0.5px;
    z-index: 2;
  }
  .headline span { display: block; white-space: nowrap; }
  .intro {
    position: absolute;
    left: 72px;
    top: 538px;
    width: 1080px;
    font-weight: 400;
    font-size: 22.5px;
    line-height: 34px;
    color: var(--white);
    z-index: 2;
  }
  .intro span { display: block; white-space: nowrap; }
  .fiber-visual {
    position: absolute;
    left: 0;
    top: 640px;
    width: 1200px;
    height: 560px;
    z-index: 1;
    background:
      radial-gradient(ellipse 55% 45% at 50% 45%, rgba(57,198,232,0.55), rgba(31,143,224,0.35) 45%, transparent 75%),
      radial-gradient(ellipse 70% 70% at 45% 80%, var(--fiber-bright), var(--fiber-deep) 60%, transparent 90%),
      linear-gradient(180deg, var(--bg) 0%, #0b1a33 45%, #0a2450 100%);
  }
</style>
</head>
<body>
  <div class="ad">
    <div class="brand">
      <div class="brand-dot"></div>
      <div class="brand-name">Brimfox Networks</div>
    </div>

    <h1 class="headline">
      <span>Fast and reliable</span>
      <span>internet service designed</span>
      <span>and catered to</span>
      <span>meet your needs</span>
    </h1>

    <p class="intro">
      <span>Brimfox Networks offers fast and reliable internet service without the headaches.</span>
      <span>No long term contracts or special promotions that expire and raise your rate. We offer a</span>
      <span>simple monthly rate with bills and features that are easy to understand.</span>
    </p>

    <div class="fiber-visual" role="img" aria-label="Close-up photograph of glowing blue fiber optic strands fanning upward"></div>
  </div>
</body>
</html>
```